Design Executive Business Acquisitons Brokerage Website

Modern but Professional with the colours black, purple and white. Must convey authenticity, and progressive out-of-square thinking. We are a boutique Business Broking firm located in Brisbane QLD Australia. We market and sell businesses with sales revenue/turnover from Au $1M to $15 M + or have a minimum staff of 15 to 50 staff. Our buyers are generally acquisitions corporate buyers. We need a modern approach but conservative tones. We are serious and experienced. We say it as it is and we get the job done! We sell in the following industries but not limited to, engineering, manufacturing, agriculture, recruitment, transportation, warehousing, services, IT,eCommerce, civil construction,mining, wholesaling, dealerships, MEdical (all), service stations, Management rights, high-end retail, building construction,importing,exporting to name a few.

Target Market(s)

SME Corporate Public & Private exsisting large businesses that are looking to buy through acquisitions

Industry/Entity Type

Coommercial executive Business Sale

Number of Pages Required

5+ page

Font styles to use
Sans Serif

Requirements
Must have
• Serious tones, searchar, NDA form, serious corporate executive feel. Include all corporaate colors,black less whit purples.Corporate Logo
Nice to have
• carosel moving right to left of industry pictures as per above and attached industries
Should not have
• No hand shaking, business people.

```html
<!DOCTYPE html>
<html lang="en">
<head>
<meta charset="utf-8">
<title>Contact Us – Meridian Brokerage</title>
<link rel="stylesheet" href="https://fonts.googleapis.com/css2?family=Outfit:wght@400;500;600&family=Open+Sans:wght@400;600&display=swap">
<style>
:root{
  --purple:#5e4590;
  --purple-dark:#4b3477;
  --ink:#222;
  --text:#555;
  --soft:#f6f6f8;
  --dark:#333;
  --white:#fff;
}
*{box-sizing:border-box;margin:0;padding:0}
html,body{width:1200px;height:2355px;overflow:hidden}
body{position:relative;font-family:"Open Sans",sans-serif;color:var(--ink);background:var(--white)}
.abs{position:absolute}
.head{font-family:"Outfit",sans-serif}
/* top bar */
.topbar{left:0;top:0;width:1200px;height:37px;background:var(--purple);color:#fff;font-size:12px}
.topbar .item{position:absolute;top:11px;display:flex;align-items:center;gap:8px}
.topbar .sep{position:absolute;top:8px;width:1px;height:21px;background:rgba(255,255,255,.35)}
.topbar .dot{position:absolute;top:13px;width:10px;height:10px;border-radius:50%;border:1.5px solid #fff}
/* header */
.header{left:0;top:37px;width:1200px;height:75px;background:#fff;box-shadow:0 2px 6px rgba(0,0,0,.04)}
.brand{position:absolute;left:44px;top:22px;display:flex;align-items:center;gap:10px;font-family:"Outfit",sans-serif;font-weight:600;font-size:25px;color:var(--purple)}
.brand .mark{width:26px;height:26px;border-radius:50%;background:var(--purple)}
.nav{position:absolute;left:359px;top:29px;display:flex;gap:26px;font-family:"Outfit",sans-serif;font-size:14px;color:var(--ink)}
.nav .active{color:var(--purple)}
.search{position:absolute;left:900px;top:19px;width:249px;height:36px;border:1.5px solid var(--purple);border-radius:18px;font-size:13px;color:#888;padding:9px 15px}
.search svg{position:absolute;right:13px;top:9px}
/* hero */
.hero{left:0;top:112px;width:1200px;height:348px;background:linear-gradient(100deg,#f1ece9 0%,#e4d3c9 35%,#cdd3d8 60%,#e9ecef 85%,#f3f2f0 100%)}
.hero h1{position:absolute;left:99px;top:130px;font-family:"Outfit",sans-serif;font-weight:500;font-size:52px;color:#333}
.crumbs{position:absolute;left:99px;top:195px;font-size:14px;color:#333;display:flex;gap:17px;align-items:center}
.crumbs i{width:1px;height:18px;background:#bbb;display:block}
/* decorative shapes */
.blob{background:var(--soft);border-radius:50%}
/* cards */
.card{top:572px;width:310px;height:244px;background:#fff;border-radius:10px;box-shadow:0 4px 22px rgba(0,0,0,.05);text-align:center}
.card svg{margin-top:50px}
.card h3{font-family:"Outfit",sans-serif;font-weight:400;font-size:22px;margin-top:18px;color:#222}
.card p{font-size:14px;color:var(--text);line-height:23px;margin-top:6px}
/* form */
.kicker{left:0;width:1200px;top:906px;text-align:center;font-family:"Outfit",sans-serif;font-size:19px}
.title{left:0;width:1200px;top:928px;text-align:center;font-family:"Outfit",sans-serif;font-weight:600;font-size:45px}
.title span{color:var(--purple)}
.label{font-size:13px;font-weight:600;color:#222}
.field{height:43px;border:1px solid var(--purple);border-radius:22px;background:#fff;font-size:12px;color:#666;padding:13px 18px}
.field svg{position:absolute;right:16px;top:14px}
.area{left:232px;top:1122px;width:740px;height:192px;border-radius:10px;border:1px solid var(--purple);background:#fff;font-size:12px;color:#666;padding:14px 18px}
.area svg{position:absolute;right:12px;top:12px}
.submit{left:516px;top:1360px;width:168px;height:40px;background:var(--purple);color:#fff;border-radius:20px;font-size:12px;font-weight:600;text-align:center;line-height:40px;letter-spacing:.3px}
/* map */
.map{left:0;top:1492px;width:1200px;height:411px;background:linear-gradient(90deg,#cfe5cf 0%,#d7e6d4 40%,#e9ebe6 58%,#a9c5f2 72%,#9fc0f5 100%)}
/* footer */
.footer{left:0;top:1903px;width:1200px;height:401px;background:linear-gradient(135deg,#5f4592,#4a3376);color:#fff}
.news-title{position:absolute;left:152px;top:86px;font-family:"Outfit",sans-serif;font-weight:500;font-size:27px}
.news-form{position:absolute;left:618px;top:79px;width:482px;height:43px;background:#fff;border-radius:22px;font-size:13px;color:#777;padding:13px 24px}
.news-form b{position:absolute;right:2px;top:2px;width:120px;height:39px;background:#2a2a2a;color:#fff;border-radius:20px;font-weight:600;text-align:center;line-height:39px}
.fcol{position:absolute;top:200px;font-size:12px;line-height:22px}
.fcol h4{font-family:"Outfit",sans-serif;font-weight:500;font-size:17px;margin-bottom:14px}
.fbrand{position:absolute;left:100px;top:205px;display:flex;align-items:center;gap:9px;font-family:"Outfit",sans-serif;font-weight:600;font-size:25px}
.fbrand .mark{width:26px;height:26px;border-radius:50%;background:#fff}
.contact-line{display:flex;align-items:center;gap:7px}
.social{display:flex;gap:17px;margin-bottom:14px}
.social span{width:27px;height:27px;border:1px solid rgba(255,255,255,.8);border-radius:50%;display:block}
.bottom{left:0;top:2304px;width:1200px;height:51px;background:var(--dark);color:#fff;font-size:12px}
</style>
</head>
<body>

<div class="abs topbar">
  <div class="item" style="left:706px">
    <svg width="14" height="10" viewBox="0 0 14 10"><rect x=".5" y=".5" width="13" height="9" fill="none" stroke="#fff"/><path d="M.5 .5l6.5 5 6.5-5" fill="none" stroke="#fff"/></svg>
    hello@meridianbrokerage.com.au</div>
  <div class="sep" style="left:902px"></div>
  <div class="item" style="left:922px">
    <svg width="11" height="11" viewBox="0 0 24 24"><path fill="#fff" d="M6.6 10.8a15 15 0 006.6 6.6l2.2-2.2c.3-.3.7-.4 1-.2 1.1.4 2.3.6 3.6.6.6 0 1 .4 1 1V20c0 .6-.4 1-1 1C10.6 21 3 13.4 3 4c0-.6.4-1 1-1h3.5c.6 0 1 .4 1 1 0 1.3.2 2.5.6 3.6.1.3 0 .7-.2 1z"/></svg>
    +61 7 3000 4821</div>
  <div class="sep" style="left:1038px"></div>
  <span class="dot" style="left:1058px"></span>
  <span class="dot" style="left:1083px"></span>
  <span class="dot" style="left:1111px"></span>
  <span class="dot" style="left:1139px"></span>
</div>

<div class="abs header">
  <div class="brand"><span class="mark"></span>Meridian Brokerage</div>
  <nav class="nav">
    <span>Home</span><span class="active">About Us</span><span>Industries</span><span>Business For Sale</span><span>Blog</span><span>Contact Us</span>
  </nav>
  <div class="search">Search here....
    <svg width="15" height="15" viewBox="0 0 16 16"><circle cx="7" cy="7" r="5.5" fill="none" stroke="#333" stroke-width="1.5"/><path d="M11 11l4 4" stroke="#333" stroke-width="1.5"/></svg>
  </div>
</div>

<div class="abs hero" role="img" aria-label="Photo of a hand tapping a smartphone screen">
  <h1>Contact Us</h1>
  <div class="crumbs"><span>Home</span><i></i><span>Contact Us</span></div>
</div>

<div class="abs blob" style="left:-420px;top:548px;width:822px;height:900px"></div>
<div class="abs blob" style="left:1012px;top:400px;width:800px;height:820px"></div>

<div class="abs card" style="left:100px">
  <svg width="58" height="58" viewBox="0 0 58 58"><path fill="#5e4590" d="M29 3l11 8H18zM6 20l23 16 23-16v33H6z"/><rect x="14" y="10" width="30" height="22" rx="3" fill="#5e4590"/><rect x="19" y="16" width="20" height="3" fill="#fff"/><rect x="19" y="22" width="20" height="3" fill="#fff"/><path d="M6 20l23 16 23-16" fill="none" stroke="#fff" stroke-width="2"/></svg>
  <h3>Email Address</h3>
  <p>deals@meridianbrokerage.com.au<br>contact@example.com</p>
</div>
<div class="abs card" style="left:445px">
  <svg width="58" height="58" viewBox="0 0 24 24"><path fill="#5e4590" d="M6.6 10.8a15 15 0 006.6 6.6l2.2-2.2c.3-.3.7-.4 1-.2 1.1.4 2.3.6 3.6.6.6 0 1 .4 1 1V20c0 .6-.4 1-1 1C10.6 21 3 13.4 3 4c0-.6.4-1 1-1h3.5c.6 0 1 .4 1 1 0 1.3.2 2.5.6 3.6.1.3 0 .7-.2 1z"/><path d="M14 3a7 7 0 017 7M14 6.5a3.5 3.5 0 013.5 3.5" fill="none" stroke="#5e4590" stroke-width="1.8" stroke-linecap="round"/></svg>
  <h3>Phone Number</h3>
  <p>+61 7 3000 4821<br>+61 7 3000 4822</p>
</div>
<div class="abs card" style="left:790px">
  <svg width="58" height="58" viewBox="0 0 24 24"><path fill="#5e4590" d="M12 1.5a7.5 7.5 0 00-7.5 7.5c0 5.6 7.5 13.5 7.5 13.5S19.5 14.6 19.5 9A7.5 7.5 0 0012 1.5zm0 10a2.6 2.6 0 110-5.2 2.6 2.6 0 010 5.2z"/></svg>
  <h3>Office Address</h3>
  <p>48 Harbour Lane,<br>Brisbane QLD Australia</p>
</div>

<div class="abs kicker">Connect With Us</div>
<div class="abs title">Get In <span>Touch</span></div>

<div class="abs label" style="left:232px;top:1005px">Your Name</div>
<div class="abs field" style="left:232px;top:1029px;width:357px">Your Name
  <svg width="12" height="14" viewBox="0 0 12 14"><circle cx="6" cy="3.5" r="3" fill="#5e4590"/><path d="M0 14c0-4 2.7-6 6-6s6 2 6 6z" fill="#5e4590"/></svg>
</div>
<div class="abs label" style="left:614px;top:1005px">Your Email</div>
<div class="abs field" style="left:614px;top:1029px;width:357px">Your Email
  <svg width="14" height="10" viewBox="0 0 14 10"><rect width="14" height="10" fill="#5e4590"/><path d="M0 0l7 5.5L14 0M0 10l5-4.5M14 10L9 5.5" fill="none" stroke="#fff" stroke-width="1"/></svg>
</div>
<div class="abs label" style="left:232px;top:1098px">Your Message</div>
<div class="abs area">Enter Your Message
  <svg width="16" height="16" viewBox="0 0 16 16"><path d="M7 2H2v12h12V9" fill="none" stroke="#5e4590" stroke-width="1.6"/><path d="M13 1.5l1.5 1.5L8 9.5 6 10l.5-2z" fill="#5e4590"/></svg>
</div>
<div class="abs submit">SUBMIT</div>

<div class="abs map" role="img" aria-label="Street map of Brisbane with the office location pinned"></div>

<div class="abs footer">
  <svg style="position:absolute;left:100px;top:88px" width="28" height="28" viewBox="0 0 58 58"><path fill="#fff" d="M29 3l11 8H18zM6 20l23 16 23-16v33H6z"/><rect x="14" y="10" width="30" height="22" rx="3" fill="#fff"/><rect x="19" y="16" width="20" height="3" fill="#5e4590"/><rect x="19" y="22" width="20" height="3" fill="#5e4590"/></svg>
  <div class="news-title">Subscribe to our Newsletter</div>
  <div class="news-form">Your Email<b>Subscribe</b></div>

  <div class="fbrand"><span class="mark"></span>Meridian Brokerage</div>
  <div class="fcol" style="left:100px;top:268px">
    <div class="contact-line">
      <svg width="9" height="9" viewBox="0 0 24 24"><path fill="#fff" d="M6.6 10.8a15 15 0 006.6 6.6l2.2-2.2c.3-.3.7-.4 1-.2 1.1.4 2.3.6 3.6.6.6 0 1 .4 1 1V20c0 .6-.4 1-1 1C10.6 21 3 13.4 3 4c0-.6.4-1 1-1h3.5c.6 0 1 .4 1 1 0 1.3.2 2.5.6 3.6.1.3 0 .7-.2 1z"/></svg>+61-7-3000-4821</div>
    <div class="contact-line" style="margin-top:2px">
      <svg width="9" height="7" viewBox="0 0 14 10"><rect width="14" height="10" fill="#fff"/></svg>office@meridianbrokerage.com.au</div>
    <div class="contact-line" style="margin-top:2px">
      <svg width="8" height="10" viewBox="0 0 24 24"><path fill="#fff" d="M12 1.5a7.5 7.5 0 00-7.5 7.5c0 5.6 7.5 13.5 7.5 13.5S19.5 14.6 19.5 9A7.5 7.5 0 0012 1.5z"/></svg>48 Harbour Lane, Brisbane</div>
  </div>

  <div class="fcol" style="left:392px">
    <h4>Our Services</h4>
    Selling a Business<br>Business Valuation<br>Business Acquisition<br>Capital Raising<br>Business Advisory
  </div>
  <div class="fcol" style="left:648px">
    <h4>Usefull Link</h4>
    Home<br>About Us<br>Business for Sale<br>Blog<br>Contact Us
  </div>
  <div class="fcol" style="left:880px;width:225px">
    <h4>Follow US</h4>
    <div class="social"><span></span><span></span><span></span><span></span></div>
    <div style="line-height:19px">Lorem ipsum dolor sit amet, consectetur adipiscing elit, sed do eiusmod tempor incididunt ut labore....</div>
  </div>
</div>

<div class="abs bottom">
  <span class="abs" style="left:100px;top:18px">2022 All rights reserved</span>
  <span class="abs" style="left:880px;top:18px">Privacy Policy</span>
  <span class="abs" style="left:995px;top:18px">Terms &amp; Conditions</span>
</div>

</body>
</html>
```